Bright tap water company advertisment

We want to design a 1/3 page A4 mini ad for a magazine AND a full a4 page brochure that will be an email attachment. The mini ad can be a simpler version of the A4.

The company is Bright Tap Flow, we sell Thermolia heat pumps and Raydeck solar hot water units.

I have attached a copy of the brochure of the units we sell as well as the logo and a few screen shots of our website that is not quite finished, our pantone colours are forest, basil and grass.

Our slogan is 'maximum heat, Minimum impact'

and then a picture of a heat pump and a picture of a solar hot water unit somewhere.
it needs to say the following:
Start your journey today towards a greener tomorrow with Raydeck or Thermolia
Up to 71% more economical than traditional units
Rebates up to $2000 may apply
contact 1300 47 61 52 for details
Brighttapflow.com.au

Raydeck Solar Hot Water
 Tanks manufactured in Australia and Holland
 Copper collectors which are the most efficient on the market
 Circulation Pump manufactured in Europe
 All standard installation parts included – no hidden costs
 Standard Solar Thermostat & 2.4kw Element (available at any plumbing supplier)
 Warranty – 7 year tank and panel

Thermolia Heat Pump
 Draw 0.6kw of power
 Require only a standard weather proof power point
 Has a back up element.
 Dual anodes for extra corrosion resistance.
 Warranty – 5 year tank, 3 years refrigerant components

Target Market(s)

the public

Industry/Entity Type

plumbing

Font styles to use
Sans Serif

Requirements
Must have
• simplicity and creativity

```html
<!DOCTYPE html>
<html lang="en">
<head>
<meta charset="utf-8">
<title>Bright Tap Flow – Maximum Heat Minimum Impact</title>
<link href="https://fonts.googleapis.com/css2?family=Montserrat:wght@500;600;900&family=Ubuntu:wght@400;700&family=Hind:wght@400&family=Open+Sans:wght@600&display=swap" rel="stylesheet">
<style>
  :root{
    --forest:#1b6b21;
    --basil:#4caa5e;
    --grass:#96ca63;
    --band-end:#5e9b62;
    --teal:#2a9d8a;
    --teal-end:#67bc74;
    --ink:#1b1b1b;
    --white:#ffffff;
    --steel:#c4c6c8;
  }
  html,body{margin:0;padding:0;width:1200px;height:1200px;overflow:hidden;background:#fff;}
  .stage{position:relative;width:1200px;height:1200px;}
  .flyer{
    position:absolute;left:152px;top:20px;width:1320px;height:1710px;
    transform:scale(0.6784);transform-origin:0 0;
    background:var(--white);overflow:hidden;
    font-family:"Open Sans",sans-serif;
  }
  .hero-band{
    position:absolute;left:0;top:0;width:915px;height:609px;
    background:linear-gradient(90deg,var(--grass) 0%,#82b865 50%,var(--band-end) 100%);
    clip-path:polygon(0 0,100% 0,100% 100%,0 100%);
  }
  .hero-band-tail{position:absolute;left:0;top:0;width:1320px;height:609px;}
  .slogan{
    position:absolute;left:68px;top:55px;margin:0;
    font-family:"Montserrat",sans-serif;font-weight:900;
    font-size:133px;line-height:123px;letter-spacing:-4px;
  }
  .slogan span{display:block;}
  .slogan .dark{color:var(--forest);}
  .slogan .light{color:var(--white);}
  .brand{
    position:absolute;left:905px;top:270px;display:flex;align-items:center;gap:14px;
  }
  .brand-dot{width:34px;height:34px;border-radius:50%;background:var(--basil);}
  .brand-name{font-family:"Ubuntu",sans-serif;font-weight:700;font-size:38px;color:var(--basil);}
  .features{position:absolute;left:0;top:0;}
  .feature{position:absolute;width:160px;text-align:center;}
  .feature .badge{
    width:108px;height:108px;margin:0 auto;border-radius:50%;
    background:var(--forest);box-shadow:4px 6px 10px rgba(0,0,0,.28);
    display:flex;align-items:center;justify-content:center;
  }
  .feature .label{margin-top:20px;font-size:16px;line-height:21px;font-weight:600;color:#222;}
  .product-photo{
    position:absolute;left:959px;top:696px;width:288px;height:450px;border-radius:10px 10px 18px 18px;
    background:linear-gradient(90deg,#b7b9bb 0%,#eeeff0 45%,#d2d3d5 70%,#a9abad 100%);
  }
  .product-pipes{position:absolute;left:1062px;top:1146px;width:90px;height:170px;
    background:linear-gradient(90deg,transparent 0 8px,#d9dbdd 8px 22px,transparent 22px 64px,#d9dbdd 64px 78px,transparent 78px);}
  .warranty{position:absolute;left:0;top:1114px;width:1320px;height:150px;}
  .warranty-item{position:absolute;top:1140px;color:var(--white);}
  .warranty-item .years{font-family:"Ubuntu",sans-serif;font-weight:700;font-size:54px;line-height:60px;color:var(--basil);}
  .warranty-item .scope{font-family:"Ubuntu",sans-serif;font-size:23px;margin-top:2px;}
  .warranty-divider{position:absolute;left:389px;top:1134px;height:108px;border-left:2px dashed #cfcfcf;}
  .specs{
    position:absolute;left:0;top:1263px;width:1320px;height:335px;
    background:linear-gradient(90deg,var(--teal) 0%,#43a886 45%,var(--teal-end) 100%);
  }
  .spec-col{position:absolute;top:35px;color:var(--white);font-family:"Hind",sans-serif;}
  .spec-col h2{margin:0 0 16px;font-family:"Ubuntu",sans-serif;font-weight:700;font-size:25px;}
  .spec-col ul{list-style:none;margin:0;padding:0;}
  .spec-col li{position:relative;padding-left:30px;font-size:16.5px;line-height:20.5px;margin-bottom:12px;max-width:450px;}
  .spec-col li svg{position:absolute;left:0;top:2px;}
  .contact{position:absolute;top:1598px;left:0;width:1320px;height:112px;}
  .contact-item{position:absolute;top:34px;display:flex;align-items:center;gap:10px;
    font-family:"Montserrat",sans-serif;font-weight:500;font-size:27px;color:var(--ink);}
</style>
</head>
<body>
<div class="stage">
  <div class="flyer">
    <svg class="hero-band-tail" viewBox="0 0 1320 609" aria-hidden="true">
      <defs>
        <linearGradient id="bandGrad" x1="0" x2="1">
          <stop offset="0" stop-color="#96ca63"/>
          <stop offset="0.55" stop-color="#82b865"/>
          <stop offset="1" stop-color="#5e9b62"/>
        </linearGradient>
      </defs>
      <polygon points="0,0 960,0 860,609 0,609" fill="url(#bandGrad)"/>
    </svg>

    <h1 class="slogan">
      <span class="dark">MAXIMUM</span>
      <span class="light">HEAT</span>
      <span class="dark">MINIMUM</span>
      <span class="light">IMPACT</span>
    </h1>

    <div class="brand"><span class="brand-dot"></span><span class="brand-name">Bright Tap Flow</span></div>

    <div class="features">
      <div class="feature" style="left:44px;top:670px">
        <div class="badge"><svg width="64" height="64" viewBox="0 0 64 64" fill="none" stroke="#fff" stroke-width="2.5"><path d="M10 34 L32 14 L54 34"/><path d="M16 30 V54 H48 V30"/><path d="M28 54 V42 H36 V54"/></svg></div>
        <div class="label">ECO<br>POWER</div>
      </div>
      <div class="feature" style="left:196px;top:670px">
        <div class="badge"><svg width="64" height="64" viewBox="0 0 64 64" fill="none" stroke="#fff" stroke-width="2.5"><path d="M10 32 A22 22 0 0 1 54 32 Z"/><path d="M32 32 V50"/><path d="M10 54 Q32 44 54 54"/></svg></div>
        <div class="label">SMARI<br>VACATION</div>
      </div>
      <div class="feature" style="left:354px;top:670px">
        <div class="badge"><svg width="64" height="64" viewBox="0 0 64 64" fill="none" stroke="#fff" stroke-width="2.5"><circle cx="32" cy="28" r="12"/><circle cx="32" cy="28" r="4"/><path d="M32 12 V16 M32 40 V44 M16 28 H20 M44 28 H48"/><path d="M26 52 H38"/></svg></div>
        <div class="label">SMART<br>BOOST</div>
      </div>
      <div class="feature" style="left:507px;top:670px">
        <div class="badge"><svg width="64" height="64" viewBox="0 0 64 64" fill="none" stroke="#fff" stroke-width="2.5"><path d="M12 26 H20 L32 16 V48 L20 38 H12 Z"/><path d="M40 26 L50 38 M50 26 L40 38"/></svg></div>
        <div class="label">LOW<br>NOISE</div>
      </div>
      <div class="feature" style="left:662px;top:670px">
        <div class="badge"><svg width="64" height="64" viewBox="0 0 64 64" fill="none" stroke="#fff" stroke-width="3"><circle cx="32" cy="32" r="9"/><path d="M32 14 V20 M32 44 V50 M14 32 H20 M44 32 H50 M19 19 L23 23 M41 41 L45 45 M45 19 L41 23 M23 41 L19 45"/></svg></div>
        <div class="label">HICT<br>EFFICIENCY</div>
      </div>

      <div class="feature" style="left:44px;top:898px">
        <div class="badge"><svg width="64" height="64" viewBox="0 0 64 64" fill="none" stroke="#fff" stroke-width="2.5"><path d="M32 10 L50 17 V32 C50 44 40 51 32 54 C24 51 14 44 14 32 V17 Z"/><path d="M32 22 V44 M22 28 L42 38 M42 28 L22 38"/></svg></div>
        <div class="label">FROST<br>PROOF</div>
      </div>
      <div class="feature" style="left:196px;top:898px">
        <div class="badge"><svg width="64" height="64" viewBox="0 0 64 64" fill="none" stroke="#fff" stroke-width="2.5"><path d="M8 28 Q32 20 56 28 L50 46 Q32 40 14 46 Z"/><path d="M24 20 Q20 30 24 40 M32 18 Q28 30 32 40 M40 20 Q36 30 40 40"/></svg></div>
        <div class="label">ANTI<br>FREEZE</div>
      </div>
      <div class="feature" style="left:354px;top:898px">
        <div class="badge"><svg width="64" height="64" viewBox="0 0 64 64" fill="none" stroke="#fff" stroke-width="2.5"><circle cx="32" cy="32" r="11"/><path d="M32 10 V18 M32 46 V54 M10 32 H18 M46 32 H54 M16 16 L22 22 M48 48 L42 42 M48 16 L42 22 M16 48 L22 42"/></svg></div>
        <div class="label" style="font-size:15px;line-height:19px">OVERHEAT<br>PROOF</div>
      </div>
      <div class="feature" style="left:507px;top:898px">
        <div class="badge"><svg width="64" height="64" viewBox="0 0 64 64" fill="none" stroke="#fff" stroke-width="3"><path d="M8 30 L30 14 L56 30"/><path d="M14 26 V48 H54"/><path d="M30 42 V48 M38 42 V48 M46 42 V48"/></svg></div>
        <div class="label" style="font-size:15px;line-height:19px">LECIONELLA<br>RROOF</div>
      </div>
      <div class="feature" style="left:662px;top:898px">
        <div class="badge"><svg width="64" height="64" viewBox="0 0 64 64" fill="none" stroke="#fff" stroke-width="2.5"><rect x="16" y="30" width="32" height="16" rx="3"/><path d="M10 50 H54"/><path d="M32 12 C24 20 38 22 32 30 C40 26 40 18 32 12 Z"/></svg></div>
        <div class="label" style="font-size:15px;line-height:19px">MICRO<br>CHANNEL</div>
      </div>
    </div>

    <svg class="warranty" viewBox="0 0 1320 150" aria-hidden="true">
      <path d="M0 0 H760 C800 0 800 40 805 70 C812 115 840 132 900 132 H1320 V150 H0 Z" fill="#1b1b1b"/>
    </svg>
    <div class="warranty-item" style="left:70px">
      <div class="years">5 YEARS</div>
      <div class="scope">Tank Cylinder &amp;Compressor</div>
    </div>
    <div class="warranty-divider"></div>
    <div class="warranty-item" style="left:442px">
      <div class="years">1 YEAR</div>
      <div class="scope" style="letter-spacing:1px">Electronics, Parts &amp; Labour</div>
    </div>

    <section class="specs">
      <div class="spec-col" style="left:70px">
        <h2>Raydeck Solar Hot Water</h2>
        <ul>
          <li><svg width="18" height="18" viewBox="0 0 18 18" fill="none" stroke="#fff" stroke-width="1.4"><circle cx="9" cy="9" r="7.5"/><path d="M5.5 9.2 L8 11.5 L12.5 6.5"/></svg>Tanks manufactured in Australia and Holland</li>
          <li><svg width="18" height="18" viewBox="0 0 18 18" fill="none" stroke="#fff" stroke-width="1.4"><circle cx="9" cy="9" r="7.5"/><path d="M5.5 9.2 L8 11.5 L12.5 6.5"/></svg>Copper collectors which are the most efficient on the market</li>
          <li><svg width="18" height="18" viewBox="0 0 18 18" fill="none" stroke="#fff" stroke-width="1.4"><circle cx="9" cy="9" r="7.5"/><path d="M5.5 9.2 L8 11.5 L12.5 6.5"/></svg>Circulation Pump manufactured in Europe</li>
          <li><svg width="18" height="18" viewBox="0 0 18 18" fill="none" stroke="#fff" stroke-width="1.4"><circle cx="9" cy="9" r="7.5"/><path d="M5.5 9.2 L8 11.5 L12.5 6.5"/></svg>All standard installation parts included – no hidden costs</li>
          <li><svg width="18" height="18" viewBox="0 0 18 18" fill="none" stroke="#fff" stroke-width="1.4"><circle cx="9" cy="9" r="7.5"/><path d="M5.5 9.2 L8 11.5 L12.5 6.5"/></svg>Standard Solar Thermostat &amp; 2.4kw Element (available at any plumbing supplier)</li>
          <li><svg width="18" height="18" viewBox="0 0 18 18" fill="none" stroke="#fff" stroke-width="1.4"><circle cx="9" cy="9" r="7.5"/><path d="M5.5 9.2 L8 11.5 L12.5 6.5"/></svg>Warranty – 7 year tank and panel</li>
        </ul>
      </div>
      <div class="spec-col" style="left:716px">
        <h2>Thermolia Heat Pump</h2>
        <ul>
          <li><svg width="18" height="18" viewBox="0 0 18 18" fill="none" stroke="#fff" stroke-width="1.4"><circle cx="9" cy="9" r="7.5"/><path d="M5.5 9.2 L8 11.5 L12.5 6.5"/></svg>Draw 0.6kw of power</li>
          <li><svg width="18" height="18" viewBox="0 0 18 18" fill="none" stroke="#fff" stroke-width="1.4"><circle cx="9" cy="9" r="7.5"/><path d="M5.5 9.2 L8 11.5 L12.5 6.5"/></svg>Require only a standard weather proof power point</li>
          <li><svg width="18" height="18" viewBox="0 0 18 18" fill="none" stroke="#fff" stroke-width="1.4"><circle cx="9" cy="9" r="7.5"/><path d="M5.5 9.2 L8 11.5 L12.5 6.5"/></svg>Has a back up elemen.</li>
          <li><svg width="18" height="18" viewBox="0 0 18 18" fill="none" stroke="#fff" stroke-width="1.4"><circle cx="9" cy="9" r="7.5"/><path d="M5.5 9.2 L8 11.5 L12.5 6.5"/></svg>Dual anodes for extra corrosion resistance.</li>
          <li><svg width="18" height="18" viewBox="0 0 18 18" fill="none" stroke="#fff" stroke-width="1.4"><circle cx="9" cy="9" r="7.5"/><path d="M5.5 9.2 L8 11.5 L12.5 6.5"/></svg>All standard installation parts included – no hidden costs</li>
          <li><svg width="18" height="18" viewBox="0 0 18 18" fill="none" stroke="#fff" stroke-width="1.4"><circle cx="9" cy="9" r="7.5"/><path d="M5.5 9.2 L8 11.5 L12.5 6.5"/></svg>Warranty – 5 year tank, 3 years refrigerant components</li>
        </ul>
      </div>
    </section>

    <div class="product-photo" role="img" aria-label="Photo of a silver cylindrical hot water heat pump tank with a dial and digital display"></div>
    <div class="product-pipes" role="img" aria-label="Hot and cold water pipes below the tank"></div>

    <footer class="contact">
      <div class="contact-item" style="left:94px">
        <svg width="50" height="50" viewBox="0 0 50 50" fill="none" stroke="#2a9d8a" stroke-width="3"><path d="M10 6 L18 6 L22 16 L16 20 C19 28 24 33 32 36 L36 30 L46 34 L46 42 C46 45 43 47 40 47 C22 45 6 30 4 12 C4 9 7 6 10 6 Z"/></svg>
        <span>1300 47 61 52</span>
      </div>
      <div class="contact-item" style="left:395px">
        <svg width="62" height="46" viewBox="0 0 62 46" fill="none" stroke="#2a9d8a" stroke-width="3"><rect x="14" y="3" width="34" height="28"/><path d="M14 3 L31 18 L48 3"/><path d="M2 30 V43 H60 V30"/></svg>
        <span>Brighttapflow.gmail.com.au</span>
      </div>
      <div class="contact-item" style="left:904px">
        <svg width="62" height="56" viewBox="0 0 62 56" fill="none" stroke="#2a9d8a" stroke-width="2.5"><rect x="2" y="2" width="56" height="44" rx="3"/><path d="M2 11 H58"/><circle cx="24" cy="24" r="6"/><path d="M14 40 C14 33 34 33 34 40"/><path d="M42 28 L54 32 V42 C54 48 48 52 48 52 C48 52 42 48 42 42 Z"/></svg>
        <span>Brighttapflow.com.au</span>
      </div>
    </footer>
  </div>
</div>
</body>
</html>
```